Design a Professional Business Card for Velmora Arcs

Design a business card for Velmora Arcs, we are a National Sport Court Company.

West Region Address: 4175 Quill Harbor Ln, Suite #215 Brenmoor, Westvale 80467
East Region Address: 3817 Tamsin Rd E, Calder Bay, Southmere 34583

Target Market(s)

High End Residential & Institutional Clients

Industry/Entity Type

Design & Construction

Contact Information for Business Card

Logo/Brand/Colors/ name, number (provided in comments)

Requirements
Must have
• Colors only provided in logo
Should not have
• Any other colors not in existing logo (attached)

```html
<!DOCTYPE html>
<html lang="en">
<head>
<meta charset="utf-8">
<title>Velmora Arcs – Business Card</title>
<link rel="stylesheet" href="https://fonts.googleapis.com/css2?family=Cinzel:wght@700&family=Montserrat:wght@400;500;600;700;800&display=swap">
<style>
  :root {
    --backdrop: #686868;
    --paper: #ffffff;
    --navy: #1b3566;
    --green: #2a7d35;
    --green-deep: #146b35;
    --blue-bright: #1f5fb0;
    --faint: #edf0f2;
  }
  * { margin: 0; padding: 0; box-sizing: border-box; }
  html, body { width: 961px; height: 1200px; overflow: hidden; }
  body { background: var(--backdrop); position: relative; font-family: "Montserrat", sans-serif; }

  .card { position: absolute; left: 152px; width: 657px; height: 375px; overflow: hidden; }
  .card--front { top: 211px; background: var(--paper); }
  .card--back { top: 629px; background: linear-gradient(105deg, var(--blue-bright) 0%, #1d4c8f 45%, var(--navy) 90%); }

  .front__backdrop-circle { position: absolute; left: -70px; top: -100px; width: 290px; height: 290px; border-radius: 50%; background: var(--faint); }

  .brand { position: absolute; display: flex; align-items: center; }
  .brand__dot { border-radius: 50%; flex: none; }
  .brand__name { font-weight: 800; text-transform: uppercase; }

  .brand--front { left: 41px; top: 43px; gap: 9px; }
  .brand--front .brand__dot { width: 48px; height: 48px; background: var(--green-deep); }
  .brand--front .brand__name { color: var(--navy); font-size: 20px; letter-spacing: 2px; line-height: 1.0; }

  .brand--back { left: 128px; top: 131px; gap: 22px; }
  .brand--back .brand__dot { width: 110px; height: 110px; background: var(--green); }
  .brand--back .brand__name { color: var(--paper); font-size: 50px; letter-spacing: 3px; line-height: 46px; }

  .person { position: absolute; right: 43px; top: 49px; text-align: right; }
  .person__name { font-family: "Cinzel", serif; font-weight: 700; font-size: 16.5px; color: var(--navy); letter-spacing: 0.5px; }
  .person__role { font-weight: 400; font-size: 15px; color: var(--green); margin-top: 3px; }

  .contacts { position: absolute; left: 52px; top: 201px; color: var(--navy); }
  .contacts__phone { font-size: 18px; font-weight: 400; line-height: 26px; }
  .contacts__phone strong { font-weight: 700; }
  .contacts__line { display: flex; align-items: center; gap: 5px; font-size: 18px; line-height: 25px; }
  .contacts__line:first-of-type { margin-top: 2px; }
  .contacts__icon { width: 15px; height: 15px; flex: none; }

  .offices { position: absolute; right: 42px; top: 191px; text-align: right; color: var(--navy); font-size: 15px; line-height: 18.5px; }
  .offices__label { color: var(--green); font-weight: 600; font-size: 14px; }
  .offices__block + .offices__block { margin-top: 11px; }

  .front__rule { position: absolute; left: 0; right: 0; top: 332px; height: 2px; background: var(--green); }
  .front__band { position: absolute; left: 0; right: 0; top: 334px; bottom: 0; background: var(--navy); }
</style>
</head>
<body>
  <section class="card card--front">
    <div class="front__backdrop-circle" aria-hidden="true"></div>

    <div class="brand brand--front">
      <span class="brand__dot" aria-hidden="true"></span>
      <span class="brand__name">Velmora<br>Arcs</span>
    </div>

    <div class="person">
      <p class="person__name">DORIAN M. CALLAWAY, VCLD</p>
      <p class="person__role">CEO &amp; Founder</p>
    </div>

    <div class="contacts">
      <p class="contacts__phone"><strong>Direct:</strong> (555) 555-0147</p>
      <p class="contacts__phone"><strong>Main:</strong> 1-800-555-0192</p>
      <p class="contacts__line">
        <svg class="contacts__icon" viewBox="0 0 16 16" aria-hidden="true"><rect x="1" y="3.5" width="14" height="9" fill="var(--green)"/><path d="M1 3.5 L8 9 L15 3.5 M1 12.5 L6 7.5 M15 12.5 L10 7.5" stroke="#fff" stroke-width="1.2" fill="none"/></svg>
        dorian@velmoraarcs.com
      </p>
      <p class="contacts__line">
        <svg class="contacts__icon" viewBox="0 0 16 16" aria-hidden="true"><g fill="none" stroke="var(--green)" stroke-width="1.3"><circle cx="8" cy="8" r="6"/><ellipse cx="8" cy="8" rx="2.6" ry="6"/><path d="M2 8 H14 M3 5 H13 M3 11 H13"/></g></svg>
        www.velmoraarcs.com
      </p>
    </div>

    <div class="offices">
      <div class="offices__block">
        <p class="offices__label">West Region Address:</p>
        <p>4175 Quill Harbor Ln, Suite</p>
        <p>#215 Brenmoor, Westvale 80467</p>
      </div>
      <div class="offices__block">
        <p class="offices__label">East Region Address:</p>
        <p>3817 Tamsin Rd E, Calder Bay,</p>
        <p>Southmere 34583</p>
      </div>
    </div>

    <div class="front__rule"></div>
    <div class="front__band"></div>
  </section>

  <section class="card card--back">
    <div class="brand brand--back">
      <span class="brand__dot" aria-hidden="true"></span>
      <span class="brand__name">Velmora<br>Arcs</span>
    </div>
  </section>
</body>
</html>
```